Buch-/E-Book-Cover für SEO Experte
Zielgruppe
SEO Experte Lorenz K. Abendroth ist Geschäftsführer einer SEO Agentur in Köln und bringt nun 'Das dicke Netzsuche & Webwerbung Handbuch' auf den Markt. ein kompaktes Werk welches alle Begrifflichkeiten und Konzepte aus der Welt der SEO Optimierung und des Online Marketings einfach erläutert zum nachschlagen in typischer Lexikon Manier.
Titel: Das dicke Netzsuche & Webwerbung Handbuch
Subtitel: Alle Fragen & Begriffe aus 6 Jahren SEO Agenturarbeit einfach erklärt und kompakt zusammengefasst zum nachschlagen
Aufgabenstellung
Es soll anders sein als das dazugehörige komplementär Buch 'Pixelhaus Ranking 2031' aber dennoch im selben Stil gearbeitet sein. Es soll wie ein sehr wertiges großes altes Lexikon wirken mit vielen Seiten. Bitte auch ein stehendes 3D Cover zum normalen Druck Cover liefern.

```html
<!DOCTYPE html>
<html lang="de">
<head>
<meta charset="utf-8">
<title>Das dicke Netzsuche &amp; Webwerbung Handbuch – Cover</title>
<link rel="stylesheet" href="https://fonts.googleapis.com/css2?family=Oswald:wght@400;500;600;700&display=swap">
<style>
  :root {
    --leather-dark: #3b332d;
    --leather-mid: #4f453d;
    --leather-light: #5c5148;
    --gold: #dcb84a;
    --gold-deep: #b8922e;
    --gold-soft: rgba(220, 184, 74, 0.55);
  }
  * { box-sizing: border-box; margin: 0; padding: 0; }
  html, body {
    width: 965px;
    height: 1200px;
    overflow: hidden;
    background: var(--leather-dark);
  }
  .cover {
    position: relative;
    width: 965px;
    height: 1200px;
    background: radial-gradient(ellipse at 50% 45%, var(--leather-light) 0%, var(--leather-mid) 45%, var(--leather-dark) 100%);
    font-family: "Oswald", "Arial Narrow", sans-serif;
    color: var(--gold);
  }
  .cover__frame {
    position: absolute;
    left: 55px;
    top: 40px;
    width: 855px;
    height: 1113px;
    border: 3px solid var(--gold);
  }
  .title {
    position: absolute;
    left: 0;
    top: 0;
    width: 965px;
    height: 540px;
  }
  .title text {
    fill: var(--gold);
    font-family: "Oswald", "Arial Narrow", sans-serif;
  }
  .title__kicker { font-weight: 600; font-size: 30px; letter-spacing: 1px; }
  .title__main { font-weight: 700; }
  .title rect { fill: var(--gold); }
  .emblem {
    position: absolute;
    left: 175px;
    top: 580px;
    width: 615px;
    height: 300px;
    background: radial-gradient(ellipse at 50% 92%, var(--gold-soft) 0%, rgba(220,184,74,0.22) 40%, rgba(220,184,74,0) 72%);
  }
  .subtitle {
    position: absolute;
    left: 0;
    top: 912px;
    width: 965px;
    text-align: center;
    font-weight: 500;
    font-size: 25px;
    line-height: 31.5px;
    letter-spacing: 1px;
    text-transform: uppercase;
  }
  .cover__rule {
    position: absolute;
    left: 129px;
    width: 723px;
    height: 4px;
    background: var(--gold);
  }
  .cover__rule--bottom { top: 1059px; }
  .author {
    position: absolute;
    left: 0;
    top: 1090px;
    width: 965px;
    text-align: center;
    font-weight: 600;
    font-size: 28px;
    letter-spacing: 4px;
    text-transform: uppercase;
  }
</style>
</head>
<body>
  <main class="cover">
    <div class="cover__frame"></div>

    <svg class="title" viewBox="0 0 965 540" aria-label="Das dicke Netzsuche &amp; Webwerbung Handbuch">
      <rect x="129" y="130" width="225" height="5"/>
      <rect x="612" y="130" width="240" height="5"/>
      <text class="title__kicker" x="483" y="145" text-anchor="middle">DAS DICKE</text>
      <text class="title__main" x="147" y="290" font-size="150" textLength="705" lengthAdjust="spacingAndGlyphs">NETZSUCHE &amp;</text>
      <text class="title__main" x="147" y="422" font-size="142" textLength="705" lengthAdjust="spacingAndGlyphs">WEBWERBUNG HANDBUCH</text>
      <rect x="129" y="514" width="723" height="5"/>
    </svg>

    <div class="emblem" role="img" aria-label="Goldenes aufgeschlagenes Buch mit Strahlenkranz"></div>

    <p class="subtitle">
      Alle Fragen &amp; Begriffe<br>
      aus 6 Jahren SEO Agenturarbeit<br>
      einfach erklärt und kompakt<br>
      zusammengefasst zum nachschlagen
    </p>

    <div class="cover__rule cover__rule--bottom"></div>

    <p class="author">Lorenz K. Abendroth</p>
  </main>
</body>
</html>
```